Velimko AdAgency Presentation

We need ppt design for an ad agency re-branding, agency is based in Moscow, Russia. Our specifics is brand audit, consulting and strategy in web and offline.
We decided to do re-branding because our current agency does not answer the purpose and we need a kind of "second breath".
The idea of re-branding appeared because of many changes that happened in company: new clients, new projects level, new team.
So we'd like to promote company of changes and design should show this spirit as possible.
You may use info in attached pdf file (sorry for Russian language). Info is not so necessary, it will be replaced later.
Updates

Please use more colors than digital blue and grey!

Industry/Entity Type

Ad Agency

Requirements
Must have
• Logo is attached. Please choose one.

Ppt project should include:
- Front and last page design
- Heading and list design
- Page-separator design
- Diagram design
- Pics appearance

```html
<!DOCTYPE html>
<html lang="en">
<head>
<meta charset="utf-8">
<title>Velimko — Project Title</title>
<link rel="stylesheet" href="https://fonts.googleapis.com/css2?family=Cabin:wght@400;500;600;700&display=swap">
<style>
  :root {
    --brand-blue: #29a9e1;
    --accent-coral: #f26a4b;
    --accent-sun: #ffc83d;
    --stripe-grey: #edf1f4;
    --paper-white: #ffffff;
    --slate-grey: #7f8a8b;
    --text-white: #ffffff;
  }
  * { margin: 0; padding: 0; box-sizing: border-box; }
  html, body {
    width: 1200px;
    height: 900px;
    overflow: hidden;
    background: var(--paper-white);
  }
  .slide {
    position: relative;
    width: 1200px;
    height: 900px;
    overflow: hidden;
    font-family: "Cabin", "Gill Sans", sans-serif;
    background: var(--paper-white);
  }
  .slide-backdrop {
    position: absolute;
    inset: 0;
    width: 1200px;
    height: 900px;
    display: block;
  }
  .title-block {
    position: absolute;
    left: 104px;
    top: 212px;
    color: var(--text-white);
  }
  .project-title {
    font-size: 51px;
    font-weight: 600;
    letter-spacing: 0.5px;
    line-height: 1;
  }
  .project-summary {
    margin-top: 18px;
    font-size: 19.5px;
    font-weight: 500;
    line-height: 33px;
    width: 450px;
  }
  .brand-lockup {
    position: absolute;
    left: 936px;
    top: 556px;
    width: 210px;
    display: flex;
    flex-direction: column;
    align-items: center;
  }
  .brand-square {
    width: 92px;
    height: 92px;
    background: var(--accent-coral);
  }
  .brand-name {
    margin-top: 40px;
    font-size: 54px;
    font-weight: 400;
    color: var(--slate-grey);
    line-height: 1;
  }
  .footer-bar {
    position: absolute;
    left: 0;
    top: 843px;
    width: 1200px;
    height: 57px;
    background: var(--slate-grey);
    border-top: 5px solid var(--accent-sun);
  }
  .page-number {
    position: absolute;
    left: 1106px;
    top: 813px;
    width: 70px;
    height: 100px;
    border: 4px solid var(--slate-grey);
    border-radius: 10px;
    background: var(--paper-white);
    padding: 5px;
  }
  .page-number-tab {
    width: 100%;
    height: 100%;
    background: var(--accent-coral);
    border-radius: 5px;
    color: var(--text-white);
    font-size: 25px;
    font-weight: 700;
    display: flex;
    justify-content: center;
    padding-top: 20px;
  }
</style>
</head>
<body>
  <main class="slide">
    <svg class="slide-backdrop" viewBox="0 0 1200 900" aria-hidden="true">
      <defs>
        <pattern id="ruled-stripes" x="0" y="210" width="1200" height="34" patternUnits="userSpaceOnUse">
          <rect x="0" y="0" width="1200" height="17" fill="var(--stripe-grey)"/>
        </pattern>
      </defs>
      <rect class="stripe-field" x="0" y="200" width="1200" height="643" fill="url(#ruled-stripes)"/>
      <polygon class="diagonal-gap" points="0,717 1200,165 1200,205 0,748" fill="var(--paper-white)"/>
      <polygon class="cover-panel" points="0,0 1200,0 1200,165 0,717" fill="var(--brand-blue)"/>
    </svg>

    <header class="title-block">
      <h1 class="project-title">Project Title Here</h1>
      <p class="project-summary">Lorem ipsum dolor sit ipsum Lorem ipsum dolor sit ipsum Lorem ipsum dolor sit ipsum</p>
    </header>

    <div class="brand-lockup">
      <div class="brand-square"></div>
      <div class="brand-name">Velimko</div>
    </div>

    <footer class="footer-bar"></footer>
    <div class="page-number"><div class="page-number-tab">01</div></div>
  </main>
</body>
</html>
```